Oak & Rain Subtitle Seek the Quiet Morning Path

This is a spiritual book. It opens with a question for the readers -- Are you happy? Then proceeds to discuss the meaning of happiness, why the majority isn't and ways to achieve it. The work offers hope, and actual answers. In that regard the cover needs to relate those things.

I'm happy to contribute by answering further questions and making suggestions, however, am open to the designer letting their Spirit soar and see where it leads them.

Ask yourself the question; Am I happy, imagine finding Your happiness then designing the cover that comes from that space. Just a thought.

Work

```html
<!DOCTYPE html>
<html lang="en">
<head>
<meta charset="utf-8">
<title>Oak &amp; Rain — Book Cover</title>
<link href="https://fonts.googleapis.com/css2?family=Cormorant+SC:wght@500;600&family=Oranienbaum&family=PT+Sans&display=swap" rel="stylesheet">
<style>
  :root {
    --navy: #0c2a52;
    --navy-deep: #08214a;
    --sky-mid: #1b4f8e;
    --sky-low: #3d7fc0;
    --sea: #2c6fa3;
    --surf: #dfe9ee;
    --sand: #c9b58f;
    --ink-white: #ffffff;
    --title-shadow: #04132b;
    --author-ink: #1c335e;
    --rule: #0a1c38;
  }
  * { margin: 0; padding: 0; box-sizing: border-box; }
  html, body { width: 1200px; height: 900px; overflow: hidden; background: var(--navy); }
  .cover { position: relative; width: 1200px; height: 900px; background: var(--navy); overflow: hidden; }

  .back-cover {
    position: absolute; left: 0; top: 0; width: 545px; height: 900px;
    color: var(--ink-white); font-family: "PT Sans", sans-serif; text-align: center;
  }
  .back-blurb { position: absolute; left: 38px; width: 470px; top: 198px; font-size: 17px; line-height: 28px; }
  .back-blurb p + p { margin-top: 28px; }
  .author-profile { position: absolute; left: 38px; width: 470px; top: 594px; font-size: 17px; line-height: 28px; }
  .author-profile h2 { font-size: 17px; font-weight: 400; margin-bottom: 8px; }

  .spine { position: absolute; left: 545px; top: 0; width: 87px; height: 900px; color: var(--ink-white); overflow: hidden; }
  .spine-title {
    position: absolute; left: 12px; top: 52px; writing-mode: vertical-rl;
    font-family: "Oranienbaum", serif; white-space: nowrap; line-height: 1;
  }
  .spine-title .main { font-family: "Cormorant SC", serif; font-weight: 600; font-size: 60px; letter-spacing: 1px; }
  .spine-title .amp { font-family: "Cormorant SC", serif; font-size: 32px; }
  .spine-title .sub { font-size: 28px; letter-spacing: 0.5px; }
  .spine-author {
    position: absolute; left: 0; width: 87px; top: 818px; text-align: center;
    font-family: "Oranienbaum", serif; font-size: 18px; line-height: 34px; letter-spacing: 0;
    white-space: nowrap;
  }

  .front-cover { position: absolute; left: 632px; top: 0; width: 568px; height: 900px; overflow: hidden; }
  .front-photo {
    position: absolute; inset: 0;
    background: linear-gradient(180deg, var(--navy) 0%, var(--navy-deep) 40%, var(--sky-mid) 62%, var(--sky-low) 86%, var(--sea) 87%, var(--sea) 91%, var(--surf) 93%, var(--sand) 95%, var(--sand) 100%);
  }
  .front-rule { position: absolute; left: 0; right: 0; top: 243px; height: 1px; background: var(--rule); }
  .front-title {
    position: absolute; left: 0; width: 568px; top: 128px; text-align: center;
    font-family: "Cormorant SC", serif; font-weight: 600; color: var(--ink-white);
    font-size: 96px; line-height: 1; letter-spacing: 1px; white-space: nowrap;
    text-shadow: -7px -5px 0 var(--title-shadow);
  }
  .front-title .amp { font-size: 46px; letter-spacing: 0; }
  .front-subtitle {
    position: absolute; left: 0; width: 568px; top: 248px; text-align: center;
    font-family: "Oranienbaum", serif; color: #f2f4f7; font-size: 44px; line-height: 50px; letter-spacing: 2px;
    text-shadow: -5px -4px 0 var(--title-shadow);
  }
  .front-author {
    position: absolute; left: 0; width: 568px; top: 848px; text-align: center;
    font-family: "Oranienbaum", serif; color: var(--author-ink); font-size: 44px; letter-spacing: 2px; line-height: 1;
  }
</style>
</head>
<body>
<main class="cover">
  <section class="back-cover">
    <div class="back-blurb">
      <p>This is a spiritual book. It opens with a question for the readers -- Are you happy? Then proceeds to discuss the meaning of happiness, why the majority isn't and ways to achieve it. The work offers hope, and actual answers. In that regard the cover needs to relate those things.</p>
      <p>I'm happy to contribute by answering further questions and making suggestions, however, am open to the designer letting their Spirit soar and see where it leads them</p>
    </div>
    <div class="author-profile">
      <h2>AUTHOR'S PROFILE</h2>
      <p>Ask yourself the question; Am I happy, imagine finding Your happiness then designing the cover that comes from that space. Just a thought.</p>
    </div>
  </section>

  <section class="spine">
    <div class="spine-title"><span class="main">OAK</span><span class="amp">&amp;</span><span class="main">RAIN</span><span class="sub">: SEEK THE QUIET MORNING PATH</span></div>
    <div class="spine-author">LENA<br>MARLOWE</div>
  </section>

  <section class="front-cover">
    <div class="front-photo" role="img" aria-label="Photo of a woman leaping on a beach holding a bunch of colourful balloons against a deep blue sky"></div>
    <div class="front-rule"></div>
    <h1 class="front-title">OAK<span class="amp">&amp;</span>RAIN</h1>
    <p class="front-subtitle">SEEK THE QUIET<br>MORNING PATH</p>
    <p class="front-author">LENA MARLOWE</p>
  </section>
</main>
</body>
</html>
```